Business Card Design for Fashion Tech Startup

Dear designers, we need a business card for Asia's premier fashion tech startup.!

PebbleNest is discovery e-commerce destination for busy, discerning parents in Asia featuring leading independent designers of baby, kids fashion apparel and sustainable brands from around the world.

PebbleNest is a modern, contemporary fashion tech startup targeting well-educated, well travelled and affluent parents. We're NOT your typical kiddy store!! Our design philosophy & e-commerce site is more like Vardo.com, Omerine.com, Quintaro.com, Paddlefern.com.
Updates

Hi, size of the business card should be 84mm X 55mm. Would appreciate some business card layouts in Portrait as added consideration, i fancy the idea of a Portrait business card. What's important is that the business card should pique the receiver's interest to log onto the website to learn more. Many thanks and love forward to the designs!

Target Market(s)

Though modern, classy in look, feel & positioning, PebbleNest does possess a cheeky, fun-loving personality as depicted by its logo and the segment it targets (baby, kids) though the key decision makers i.e primarily mums between 25-40 who are well educated/travelled, local & expatriates, internet/digitally savvy, mid-high income working mums.

Industry/Entity Type

E-Commerce

Requirements
Must have
• Name, designation, email, phone & mobile number.
Company url : www.pebblenest.sg
Slogan : Discovery e-commerce destination for discerning, busy parents
Nice to have
• Call to Action such as a Discount code offering 10% discount
or asking people to "Like" us on our Facebook page/Facebook URL

```html
<!DOCTYPE html>
<html lang="en">
<head>
<meta charset="utf-8">
<title>PebbleNest Business Card</title>
<link rel="stylesheet" href="https://fonts.googleapis.com/css2?family=Fredoka:wght@600&family=Short+Stack&display=swap">
<style>
  :root {
    --bg-light: #f2f2f2;
    --bg-dark: #c9c9c9;
    --teal: #3fa393;
    --orange: #e8704f;
    --navy: #2e3d52;
    --paper: #f4f4f2;
    --ring: rgba(255,255,255,0.08);
  }
  * { margin: 0; padding: 0; box-sizing: border-box; }
  html, body { width: 1200px; height: 750px; overflow: hidden; }
  body {
    background: radial-gradient(ellipse at 40% 20%, var(--bg-light), var(--bg-dark));
    position: relative;
    font-family: "Short Stack", cursive;
  }
  .card {
    position: absolute;
    top: 210px;
    width: 504px;
    height: 330px;
    border-radius: 26px;
    overflow: hidden;
    box-shadow: 0 8px 20px rgba(0,0,0,0.22);
  }
  .card--front { left: 64px; background: var(--teal); }
  .card--back { left: 632px; background: var(--paper); }

  .decor-ring {
    position: absolute;
    width: 190px; height: 190px;
    border-radius: 50%;
    border: 22px solid var(--ring);
  }
  .card--front .decor-ring { left: 170px; top: 70px; }

  .brand-dot {
    position: absolute;
    border-radius: 50%;
    background: var(--navy);
  }
  .card--front .brand-dot { left: 36px; top: 104px; width: 92px; height: 92px; }

  .wordmark {
    position: absolute;
    font-family: "Fredoka", sans-serif;
    font-weight: 600;
    color: var(--orange);
    letter-spacing: 0.5px;
    white-space: nowrap;
    line-height: 1;
  }
  .card--front .wordmark { left: 156px; top: 46px; font-size: 44px; }

  .slogan {
    position: absolute;
    left: 150px; top: 112px;
    color: var(--navy);
    font-size: 16px;
    line-height: 1.4;
    white-space: nowrap;
  }

  .step {
    position: absolute;
    display: flex;
    align-items: center;
    gap: 8px;
    color: var(--orange);
    font-size: 10px;
    line-height: 1.2;
    white-space: nowrap;
  }
  .step__num {
    width: 20px; height: 20px;
    border-radius: 4px;
    background: var(--navy);
    color: var(--paper);
    font-size: 11px;
    display: flex; align-items: center; justify-content: center;
    flex-shrink: 0;
  }
  .step--one { left: 24px; top: 270px; }
  .step--two { left: 230px; top: 200px; }
  .step--three { left: 380px; top: 200px; }

  .back-panel { position: absolute; inset: 0; }
  .card--back .brand-dot { left: 70px; top: 106px; width: 96px; height: 96px; }
  .card--back .wordmark { left: 36px; top: 222px; font-size: 31px; }

  .person {
    position: absolute;
    right: 46px; top: 74px;
    text-align: right;
    font-family: "Fredoka", sans-serif;
    font-weight: 600;
    color: var(--orange);
    white-space: nowrap;
  }
  .person__name { font-size: 34px; line-height: 1; }
  .person__role { font-size: 16px; letter-spacing: 1px; }

  .contacts {
    position: absolute;
    left: 292px; top: 162px;
    list-style: none;
    color: var(--orange);
    font-size: 13px;
    white-space: nowrap;
  }
  .contacts li {
    display: flex; align-items: center; gap: 10px;
    height: 26px;
  }
  .contact-icon { width: 18px; height: 18px; flex-shrink: 0; }
</style>
</head>
<body>

<section class="card card--front" aria-label="Card front">
  <div class="decor-ring"></div>
  <div class="brand-dot"></div>
  <div class="wordmark">PebbleNest</div>
  <p class="slogan">Discovery e-commerce destination<br>for discerning, busy parents</p>

  <div class="step step--one"><span class="step__num">1</span><span>Browse new designers<br>Find a look you love</span></div>
  <div class="step step--two"><span class="step__num">2</span><span>Like us</span></div>
  <div class="step step--three"><span class="step__num">3</span><span>Get 10% off</span></div>
</section>

<section class="card card--back" aria-label="Card back">
  <svg class="back-panel" viewBox="0 0 504 330" preserveAspectRatio="none" aria-hidden="true">
    <path d="M210 0 C 180 50, 170 90, 215 150 C 260 210, 250 270, 220 330 L504 330 L504 0 Z" fill="var(--teal)"/>
    <path d="M210 0 C 180 50, 170 90, 215 150 C 260 210, 250 270, 220 330" fill="none" stroke="var(--orange)" stroke-width="5"/>
    <circle cx="330" cy="160" r="80" fill="none" stroke="var(--ring)" stroke-width="22"/>
  </svg>

  <div class="brand-dot"></div>
  <div class="wordmark">PebbleNest</div>

  <div class="person">
    <div class="person__name">Maren Alcott</div>
    <div class="person__role">DESIGNATION</div>
  </div>

  <ul class="contacts">
    <li>
      <svg class="contact-icon" viewBox="0 0 18 18"><circle cx="9" cy="9" r="9" fill="var(--navy)"/><path d="M6 5 L8 5 L8.6 7.4 L7.6 8.2 Q8.6 10.2 10 10.6 L10.8 9.6 L13 10.2 L13 12 Q8 13 5.5 6.5 Z" fill="var(--orange)"/></svg>
      <span>+65 6100 2040</span>
    </li>
    <li>
      <svg class="contact-icon" viewBox="0 0 18 18"><circle cx="9" cy="9" r="9" fill="var(--navy)"/><rect x="6.5" y="4" width="5" height="10" rx="1" fill="var(--orange)"/></svg>
      <span>+65 9100 3050</span>
    </li>
    <li>
      <svg class="contact-icon" viewBox="0 0 18 18"><circle cx="9" cy="9" r="9" fill="var(--navy)"/><rect x="4.5" y="6" width="9" height="6.5" fill="var(--orange)"/><path d="M4.5 6 L9 9.5 L13.5 6" fill="none" stroke="var(--navy)" stroke-width="1"/></svg>
      <span>maren@pebblenest.sg</span>
    </li>
    <li>
      <svg class="contact-icon" viewBox="0 0 18 18"><circle cx="9" cy="9" r="9" fill="var(--navy)"/><circle cx="9" cy="9" r="5" fill="none" stroke="var(--orange)" stroke-width="1.4"/><path d="M4 9 H14 M9 4 V14" stroke="var(--orange)" stroke-width="1.2"/></svg>
      <span>www.pebblenest.sg</span>
    </li>
  </ul>
</section>

</body>
</html>
```